Electronic Repair Company need a new flyer!

Hi Guys,

I need a new flyer for my repair company that I can use for my door 2 door marketing. The flyers will be send to thousands of addresses in the Netherlands. You can design the flyer in English but I need to be able to translate the flyer into Dutch, so I might need the PSD file.

We repair Computers, Laptops and ALL Velmora devices.

For some inspiration please take a look at: www.qorvatek.nl

And see the pictures below ;)

Target Market(s)

Computer & Smartphone Repair

Industry/Entity Type

Electronic

Requirements
Nice to have
• I would like to have some pictures from our staff (like on our website) in it so people can see who we really are :)

```html
<!DOCTYPE html>
<html lang="en">
<head>
<meta charset="utf-8">
<title>Qorvatek.nl Flyer</title>
<link href="https://fonts.googleapis.com/css2?family=Oswald:wght@500;700&family=Roboto:wght@400;500;700&display=swap" rel="stylesheet">
<style>
  :root{
    --red:#e8432a;
    --dark:#2e2e2e;
    --ink:#1f1f1f;
    --paper:#ffffff;
    --stage:#e9e6e2;
    --photo-light:#dfe3e6;
    --photo-mid:#9aa3aa;
  }
  *{box-sizing:border-box;margin:0;padding:0}
  html,body{width:1200px;height:1200px;overflow:hidden;background:var(--stage)}
  .flyer{position:absolute;left:185px;top:35px;width:830px;height:1130px;background:var(--paper);overflow:hidden;font-family:"Roboto",sans-serif;color:var(--ink);box-shadow:0 6px 24px rgba(0,0,0,.18)}
  .shapes{position:absolute;left:0;top:0}
  .photo-team{position:absolute;left:0;top:0;width:830px;height:600px;clip-path:polygon(0 112px,830px 217px,830px 528px,0 552px);background:linear-gradient(160deg,var(--photo-light) 0%,#c9ced2 45%,var(--photo-mid) 100%)}
  .brand{position:absolute;right:40px;top:28px;display:flex;align-items:center;gap:10px}
  .brand-mark{width:30px;height:30px;background:var(--red)}
  .brand-name{font-weight:700;font-size:42px;letter-spacing:.5px;color:var(--ink);line-height:1}
  .brand-call{position:absolute;right:40px;top:82px;font-weight:700;font-size:19px;color:var(--ink)}
  .headline{position:absolute;left:12px;top:604px;font-family:"Oswald",sans-serif;font-weight:700;font-size:58px;line-height:1;color:var(--red);letter-spacing:.5px}
  .subhead{position:absolute;left:14px;top:670px;font-weight:700;font-size:40px;line-height:1;color:var(--ink)}
  .intro-bar{position:absolute;left:0;top:738px;width:598px;height:40px;background:var(--red);color:#fff;font-weight:700;font-size:26px;letter-spacing:2.5px;padding:3px 0 0 12px}
  .intro-copy{position:absolute;left:12px;top:786px;width:560px;font-size:16.5px;line-height:19px;color:var(--ink)}
  .tagline{position:absolute;left:12px;top:888px;font-weight:700;font-size:29px;color:var(--red)}
  .footer{position:absolute;left:0;top:940px;width:815px;height:155px;background:var(--dark)}
  .promise{position:absolute;left:18px;top:948px;width:480px;height:46px;background:var(--red);border-radius:0 0 14px 14px;transform:skewX(-8deg);display:flex;align-items:center;justify-content:center}
  .promise span{transform:skewX(8deg);font-family:"Oswald",sans-serif;font-weight:500;font-size:27px;color:#fff}
  .contact{position:absolute;left:0;top:1012px;width:510px;text-align:center;color:#fff}
  .contact-label{font-size:22px;font-weight:500}
  .contact-line{font-size:30px;font-weight:500;margin-top:4px;letter-spacing:.3px}
  .partners{position:absolute;left:0;top:1095px;width:815px;height:35px;background:var(--red);display:flex;align-items:center;gap:16px;padding-left:10px}
  .partner-badge{width:56px;height:16px;border-radius:3px;background:rgba(255,255,255,.9)}
  .photo-staff{position:absolute;left:520px;top:875px;width:280px;height:255px;background:linear-gradient(180deg,#f2efea 0%,#f07a4d 55%,#d8d4cf 100%)}
  .services{position:absolute;left:600px;top:565px;width:215px;height:310px;background:var(--dark)}
  .services-title{position:absolute;left:583px;top:562px;width:237px;height:40px;background:var(--red);color:#fff;font-weight:700;font-size:29px;text-align:center;line-height:40px}
  .service-list{position:absolute;left:620px;top:614px;list-style:none}
  .service-item{display:flex;align-items:center;gap:12px;height:53px}
  .service-icon{width:26px;height:26px;background:var(--red);display:flex;align-items:center;justify-content:center}
  .service-name{color:#fff;font-weight:500;font-size:19px;line-height:18px}
  .service-name small{display:block;font-size:11px;font-weight:700;line-height:11px}
</style>
</head>
<body>
<div class="flyer">
  <div class="photo-team" role="img" aria-label="Photo of the repair staff at the service counter with laptops and a desktop computer"></div>

  <svg class="shapes" width="830" height="1130" viewBox="0 0 830 1130" aria-hidden="true">
    <polygon points="0,0 138,0 548,156 0,66" fill="#e8432a"/>
    <polygon points="0,66 830,200 830,212 0,108" fill="#2e2e2e"/>
    <polygon points="0,108 830,212 830,218 0,114" fill="#e8432a"/>
    <polygon points="0,552 830,528 830,538 0,572" fill="#2e2e2e"/>
    <polygon points="0,572 830,538 830,546 0,596" fill="#e8432a"/>
  </svg>

  <div class="brand">
    <span class="brand-mark"></span>
    <span class="brand-name">QORVATEK.NL</span>
  </div>
  <div class="brand-call">Call our customer service 088-0172630</div>

  <h1 class="headline">QUICKLY QUALITATIVELY</h1>
  <p class="subhead">AND ON A NO WIN NO FEE!</p>

  <div class="intro-bar">Pleasant, we Qorvatek.nl</div>
  <p class="intro-copy">More than 20 technicians are six days a week, ready to repair your device as soon as possible. Because we have more than 1.2 million parts center in stock, we can often fix within 24 hours of your device! With us you can go for the repair of your VelDesk or VelBook.Velmora help our specialists will be happy with a professional</p>
  <p class="tagline">We repair your social and business life!</p>

  <div class="services"></div>
  <div class="services-title">Our Service</div>
  <ul class="service-list">
    <li class="service-item">
      <span class="service-icon"><svg width="16" height="16" viewBox="0 0 16 16"><circle cx="8" cy="8" r="6" fill="#fff"/></svg></span>
      <span class="service-name">VELMORA<small>REPAIR</small></span>
    </li>
    <li class="service-item">
      <span class="service-icon"><svg width="18" height="16" viewBox="0 0 18 16"><rect x="1" y="2" width="16" height="10" fill="#fff"/><rect x="7" y="12" width="4" height="3" fill="#fff"/></svg></span>
      <span class="service-name">COMPUTER<small>REPAIR</small></span>
    </li>
    <li class="service-item">
      <span class="service-icon"><svg width="18" height="16" viewBox="0 0 18 16"><rect x="3" y="3" width="12" height="8" fill="#fff"/><rect x="1" y="12" width="16" height="2" fill="#fff"/></svg></span>
      <span class="service-name">LAPTOP<small>REPAIR</small></span>
    </li>
    <li class="service-item">
      <span class="service-icon"><svg width="16" height="18" viewBox="0 0 16 18"><rect x="2" y="1" width="12" height="16" rx="1" fill="#fff"/><rect x="4" y="3" width="8" height="11" fill="#e8432a"/></svg></span>
      <span class="service-name">TABLET<small>REPAIR</small></span>
    </li>
    <li class="service-item">
      <span class="service-icon"><svg width="12" height="18" viewBox="0 0 12 18"><rect x="2" y="1" width="8" height="16" rx="1" fill="#fff"/><rect x="3.5" y="3" width="5" height="10" fill="#e8432a"/></svg></span>
      <span class="service-name">SMARTPHONE<small>REPAIR</small></span>
    </li>
  </ul>

  <div class="footer"></div>
  <div class="promise"><span>Your device repaired within 24 hours!</span></div>
  <div class="contact">
    <p class="contact-label">Call our customer service</p>
    <p class="contact-line">088-0172630 | www.qorvatek.nl</p>
  </div>

  <div class="partners">
    <span class="partner-badge"></span><span class="partner-badge"></span><span class="partner-badge"></span>
    <span class="partner-badge"></span><span class="partner-badge"></span><span class="partner-badge"></span>
    <span class="partner-badge"></span><span class="partner-badge"></span><span class="partner-badge"></span>
  </div>

  <div class="photo-staff" role="img" aria-label="Photo of a smiling technician in an orange and white polo holding a laptop and a charger"></div>
</div>
</body>
</html>
```